Stainless Steel Business Card

I have a fiber laser and want to highlight its capabilities in a business card. On the card I want

Brisler Systems
Martin Pelko
martin@mpelkoworks.com
417-555-0136

This will be cut / engraved on stainless steel. I want the Brisler Systems to be prominent with laser cut font so that there are no dropouts on the O and A's. My name email and phone number should be engraved black. I would like some cool geometric patterns to cutout on the card to highlight the capabilities of my machine. I will need to files in the end either SVG or dxf of the engrave portion and the cut portion.

```html
<!DOCTYPE html>
<html lang="en">
<head>
<meta charset="utf-8">
<title>Brisler Systems – Business Card</title>
<link rel="stylesheet" href="https://fonts.googleapis.com/css2?family=Saira+Stencil+One&family=Arimo:wght@400;700&display=swap">
<style>
  :root {
    --backdrop: #5c5c5c;
    --card: #ffffff;
    --brand-grey: #666666;
    --name-navy: #0d0f4f;
    --detail-grey: #555555;
    --rule: #bdbdbd;
    --cutout: #5c5c5c;
  }
  * { margin: 0; padding: 0; box-sizing: border-box; }
  html, body {
    width: 1200px;
    height: 815px;
    overflow: hidden;
    background: var(--backdrop);
  }
  .card {
    position: absolute;
    left: 196px;
    top: 184px;
    width: 798px;
    height: 456px;
    background: var(--card);
  }
  .cutout-pattern {
    position: absolute;
    left: 56px;
    top: 56px;
    width: 250px;
    height: 190px;
  }
  .cutout-pattern polygon {
    fill: var(--cutout);
  }
  .brand {
    position: absolute;
    right: 55px;
    top: 46px;
    text-align: right;
    font-family: 'Saira Stencil One', sans-serif;
    font-weight: 400;
    color: var(--brand-grey);
    line-height: 1;
  }
  .brand-name {
    display: block;
    font-size: 84px;
    letter-spacing: 1px;
  }
  .brand-sub {
    display: block;
    margin-top: 2px;
    font-size: 48px;
    letter-spacing: 1px;
  }
  .person-name {
    position: absolute;
    left: 56px;
    top: 311px;
    font-family: 'Arimo', Arial, sans-serif;
    font-weight: 700;
    font-size: 33px;
    line-height: 33px;
    color: var(--name-navy);
  }
  .divider {
    position: absolute;
    left: 57px;
    top: 351px;
    width: 686px;
    height: 1px;
    background: var(--rule);
  }
  .contact {
    position: absolute;
    left: 54px;
    top: 363px;
    list-style: none;
    font-family: 'Arimo', Arial, sans-serif;
    font-size: 18px;
    line-height: 23px;
    color: var(--detail-grey);
  }
  .contact-item {
    display: flex;
    align-items: center;
    gap: 11px;
  }
  .contact-icon {
    width: 16px;
    height: 16px;
    fill: var(--name-navy);
    flex: none;
  }
</style>
</head>
<body>
  <main class="card">
    <svg class="cutout-pattern" viewBox="0 0 250 190" aria-hidden="true">
      <polygon points="20,0 40,11.5 40,34.5 20,46 0,34.5 0,11.5"/>
      <polygon points="66,0 86,11.5 86,34.5 66,46 46,34.5 46,11.5"/>
      <polygon points="112,0 132,11.5 132,34.5 112,46 92,34.5 92,11.5"/>
      <polygon points="158,4 174,13 174,31 158,40 142,31 142,13"/>
      <polygon points="202,9 213,15.5 213,28.5 202,35 191,28.5 191,15.5"/>
      <polygon points="43,40 63,51.5 63,74.5 43,86 23,74.5 23,51.5"/>
      <polygon points="89,40 109,51.5 109,74.5 89,86 69,74.5 69,51.5"/>
      <polygon points="135,44 151,53 151,71 135,80 119,71 119,53"/>
      <polygon points="180,49 191,55.5 191,68.5 180,75 169,68.5 169,55.5"/>
      <polygon points="20,80 40,91.5 40,114.5 20,126 0,114.5 0,91.5"/>
      <polygon points="66,84 82,93 82,111 66,120 50,111 50,93"/>
      <polygon points="112,89 123,95.5 123,108.5 112,115 101,108.5 101,95.5"/>
      <polygon points="43,124 54,130.5 54,143.5 43,150 32,143.5 32,130.5"/>
      <polygon points="20,162 27,166 27,174 20,178 13,174 13,166"/>
    </svg>

    <div class="brand">
      <span class="brand-name">Brisler</span>
      <span class="brand-sub">Systems</span>
    </div>

    <h1 class="person-name">Martin Pelko</h1>
    <div class="divider"></div>

    <ul class="contact">
      <li class="contact-item">
        <svg class="contact-icon" viewBox="0 0 24 24" aria-hidden="true">
          <path d="M6.6 10.8a15.1 15.1 0 0 0 6.6 6.6l2.2-2.2c.3-.3.7-.4 1-.2 1.1.4 2.3.6 3.6.6.6 0 1 .4 1 1V20c0 .6-.4 1-1 1A17 17 0 0 1 3 4c0-.6.4-1 1-1h3.5c.6 0 1 .4 1 1 0 1.3.2 2.5.6 3.6.1.3 0 .7-.2 1z"/>
        </svg>
        <span>417-555-0136</span>
      </li>
      <li class="contact-item">
        <svg class="contact-icon" viewBox="0 0 24 24" aria-hidden="true">
          <path d="M2 5.5h20V19H2z"/>
          <path d="M3 7l9 6.3L21 7" fill="none" stroke="#ffffff" stroke-width="1.6"/>
        </svg>
        <span>martin@mpelkoworks.com</span>
      </li>
    </ul>
  </main>
</body>
</html>
```